High profile consulting company needs a Business Card Design

I need a business card design for a coaching /consulting company. We specialize in changing behaviors. Our services include therapy, workshops, life coaching, etc.

Check out our website to get a feel for our personality. www.tidewaterguidance.com

The new logo will be attached to the website soon, I have attached the new logo for your use on the business card.
Updates

I forgot to provide you with the company email under the "must have" section for the business card.  The website is:

 www.tidewaterguidance.com

I understand there's some trouble with the logo I uploaded.  I will try that again.  Thank you for your efforts.

Lauren

Thank you for some of your questions.  I prefer a one sided business card, and tend to like the white backgrounds.

I also made 2 small changes to the content.  

add MFT after the name:  Lauren Pettigrew, MFT

and the tag line needed more clarity once I saw it.  Please change it to:  Improving performance by strengthening relationships and changing behaviors.

Thank you,
Lauren

Industry/Entity Type

Business

Requirements
Must have
• logo
Phone number: 321-555-0164
email: Lauren@tidewaterguidance.com
Lauren Pettigrew, MFT
President
Nice to have
• Improving performance by strengthening relationships and changing behaviors.

```html
<!DOCTYPE html>
<html lang="en">
<head>
<meta charset="UTF-8">
<title>Tidewater Guidance – Business Cards</title>
<link rel="stylesheet" href="https://fonts.googleapis.com/css2?family=Crimson+Text:ital,wght@0,600;1,400;1,600&display=swap">
<style>
  :root {
    --backdrop: #1f1f1f;
    --card-white: #ffffff;
    --brand-green: #127356;
    --ink-grey: #4a4a4a;
    --watermark: #eef0ef;
  }
  * { margin: 0; padding: 0; box-sizing: border-box; }
  html, body {
    width: 1200px;
    height: 900px;
    overflow: hidden;
    background: var(--backdrop);
    font-family: "Crimson Text", Georgia, serif;
  }
  .canvas {
    position: relative;
    width: 1200px;
    height: 900px;
  }
  .card {
    position: absolute;
    width: 600px;
    height: 350px;
    background: var(--card-white);
    overflow: hidden;
    box-shadow: 0 10px 30px rgba(0,0,0,0.55);
  }
  .card--front { left: 120px; top: 62px; }
  .card--back  { left: 470px; top: 440px; }

  /* brand lockup */
  .brand {
    position: absolute;
    display: flex;
    align-items: center;
  }
  .brand__dot {
    flex: none;
    border-radius: 50%;
    background: var(--brand-green);
  }
  .brand__name {
    color: var(--brand-green);
    font-weight: 600;
    text-transform: uppercase;
    line-height: 1;
  }
  .card--front .brand { left: 72px; top: 72px; }
  .card--front .brand__dot { width: 112px; height: 112px; margin-right: 18px; }
  .card--front .brand__name { font-size: 46px; letter-spacing: 1px; }

  .card--back .brand { left: 50px; top: 56px; }
  .card--back .brand__dot { width: 54px; height: 54px; margin-right: 10px; }
  .card--back .brand__name { font-size: 24px; letter-spacing: 0.5px; }

  /* green bands */
  .band {
    position: absolute;
    left: 0;
    right: 0;
    bottom: 0;
    background: var(--brand-green);
  }
  .card--front .band {
    height: 112px;
    display: flex;
    align-items: center;
    justify-content: center;
  }
  .tagline {
    color: var(--card-white);
    font-style: italic;
    font-weight: 600;
    font-size: 21px;
    letter-spacing: 0.2px;
  }
  .card--back .band { height: 36px; }

  /* faint decoration */
  .watermark {
    position: absolute;
    right: -110px;
    top: 20px;
    width: 300px;
    height: 300px;
  }

  /* contact block */
  .contact {
    position: absolute;
    left: 62px;
    top: 170px;
    color: var(--ink-grey);
    font-style: italic;
  }
  .contact__name { font-size: 22px; line-height: 1.1; }
  .contact__title { font-size: 15px; margin-top: 6px; }
  .contact__lines {
    list-style: none;
    margin-top: 22px;
    font-size: 15px;
    line-height: 1.45;
  }
</style>
</head>
<body>
<main class="canvas">

  <section class="card card--front" aria-label="Business card front">
    <div class="brand">
      <span class="brand__dot" aria-hidden="true"></span>
      <span class="brand__name">Tidewater Guidance</span>
    </div>
    <div class="band">
      <p class="tagline">Specializing in relationships and changing behaviors</p>
    </div>
  </section>

  <section class="card card--back" aria-label="Business card back">
    <svg class="watermark" viewBox="0 0 300 300" aria-hidden="true">
      <circle cx="150" cy="150" r="140" fill="none" stroke="var(--watermark)" stroke-width="14"/>
    </svg>
    <div class="brand">
      <span class="brand__dot" aria-hidden="true"></span>
      <span class="brand__name">Tidewater Guidance</span>
    </div>
    <div class="contact">
      <p class="contact__name">Lauren Pettigrew</p>
      <p class="contact__title">President</p>
      <ul class="contact__lines">
        <li>www.tidewaterguidance.com</li>
        <li>Lauren@tidewaterguidance.com</li>
        <li>Ph: 321-555-0164</li>
      </ul>
    </div>
    <div class="band"></div>
  </section>

</main>
</body>
</html>
```